Flyer Design Project for Harbor Tidy Works Inc.

We require a double sided marketing flyer 8 1/2 x 11. The flyer will also be marketed via e-mail using one or both sides. "Outside of the box" but yet "professional" marketing is what we'd like to achieve.

Harbor Tidy Works Inc., is a building service company providing cleaning, caretaking and concierge service to residential/stratas (condominiums/apartments)...(These services are usually provided during daytime hours). and janitorial service to commercial buildings ( service provided at night time).

- 100% green cleaning chemicals and systems
- Professionally trained staff
- Customer service is #1 priority
- Excellent Communication systems

Brochure to be 2 pages.:

Side 1: marketing residential/strata building services with a focus on providing cleaning services with a sub-focus on caretaking and concierge. We also provide move-in/out service where we coordinate with tenants to arrange access to the building, elevators and provide security (no moving involved)

Side 2: marketing night time janitorial service to property managers, corporate head offices, small offices, industrial facilities

http://www.gleamnest-home.com/index.php

http://www.brightholdpc.ca/services

These websites are from the best maid cleaning business and best strata//residential cleaning business in the city. The maid website is "you" focused, that works! The other is very straight forward and to the point, which also works.

At the end of the day our target audience ( property managers and building owners ) want us to take away one of their biggest headaches - "CLEANING". They have better things to be doing than dealing with whether or not the elevator is clean! That's our job! We're in the CLEANING business and when they don't hear a word from any of their tenants, we're doing our job and they're HAPPY :) WE TAKE AWAY HEADACHES AND MAKE PEOPLE HAPPY!

very multi-cultural target audience!

HOW CAN WE SHOW THEM IN A FLYER? THAT'S THE CHALLENGE! AND THE WINNING DESIGNER WILL BE THE ONE WHO CAN EFFECTIVELY COMMUNICATE THIS IN 1-2 PAGES.
Updates

Thank you all very much. Varolinda and Tulip, your designs are very encouraging.

Design 1223617: The layout is close to what we are hoping to achieve as it may also be incorporated into a web site homepage with each block used as a link to more info. The pictures however, make it look like any other company flyer.

Design 1224020: Also a very good layout but again not liking the pictures.

Overall, some of the designs are a little to busy with information. I would like to see something just a little more simple and yet unique that stands out against other companies.

Look forward to the second round. Thank you all very much!

Please see the new files called commercial building pics, residential strata pics and misc pics that you can use in the brochure. These are the types of pictures I would like included. Thanks.

Hi Designers

Would like to see a design that combines the layout format of the bottom half of 1234602 ( easy to read) and the top half of 1227356 ( like the pictures in this one).

Also, want to replace "Marketing....." with Side #1 " Providing residential/stratas with quality, affordable cleaning, caretaking and concierge services.. and then the rest of the text in point/bullet form.

With side #2, want to replace " Marketing...." with "Providing quality, affordable commercial janitorial service to....

                                   

 

Please use latest pictures uploaded. The designs we've liked so far have 1 large picture ( picture of buildings ) on each side with 2-3 smaller pics in various layouts. i.e. for side 1 : Cleaning ( a picture of a cleaner ) Caretaking ( picture of handyman in white shaking hand) Concierge ( picture of person at a desk on the phone)

The font should be large and easy to read. We also like the designs where key points are in point form.

The company name and logo and contact info should be easy to read.

We did like one design using vector characters but think they should only be incorporated as part of the overall design

Target Market(s)

Property Managers, Building Owners, Multicultural Decision makers, aged 28 - 60, very busy people

Industry/Entity Type

Janitorial Service

Requirements
Must have
• 2 pages, 8 1/2 x 11 ( double sided) but can be used separately
Nice to have
• Would like to be able to change photos for different campaigns

```html
<!DOCTYPE html>
<html lang="en">
<head>
<meta charset="utf-8">
<title>Harbor Tidy Works Inc. — Building Services Flyer</title>
<link href="https://fonts.googleapis.com/css2?family=Orbitron:wght@700&family=Roboto+Condensed:wght@700&display=swap" rel="stylesheet">
<style>
  :root {
    --sky: #1aaeef;
    --sky-ink: #1ea8ea;
    --sky-pale: #8fd6f7;
    --paper: #ffffff;
    --backdrop: #e7e7e9;
  }
  * { margin: 0; padding: 0; box-sizing: border-box; }
  html, body { width: 1200px; height: 787px; overflow: hidden; background: var(--backdrop); }
  body { position: relative; font-family: "Roboto Condensed", "Arial Narrow", sans-serif; font-weight: 700; color: var(--sky-ink); }

  .page { position: absolute; top: 33px; width: 557px; height: 721px; background: var(--paper); overflow: hidden; }
  .page--residential { left: 33px; }
  .page--commercial { left: 610px; }

  .title-block { position: absolute; left: 0; top: 0; width: 204px; height: 156px; background: var(--sky); color: var(--paper);
    font-family: "Orbitron", sans-serif; font-size: 13.5px; letter-spacing: 1.6px; line-height: 27.5px; padding: 19px 0 0 30px; text-transform: uppercase; }
  .contact-block { position: absolute; left: 0; bottom: 0; width: 204px; height: 156px; background: var(--sky); color: var(--paper); }

  .line { position: absolute; font-size: 19px; line-height: 25px; white-space: nowrap; text-transform: uppercase; }
  .line--plain { text-transform: none; }
  .icon { position: absolute; }

  .service-tile { position: absolute; width: 42px; height: 42px; border-radius: 7px; background: var(--sky); }

  .phone-small { position: absolute; left: 25px; top: 59px; font-size: 17px; line-height: 22px; }
  .email { position: absolute; left: 25px; top: 82px; font-size: 7px; font-weight: 700; }
  .headline { position: absolute; left: 232px; font-size: 30px; line-height: 36px; text-transform: uppercase; white-space: nowrap; }

  .call-label { position: absolute; left: 0; width: 204px; top: 50px; text-align: center; font-size: 19px; }
  .call-number { position: absolute; left: 0; width: 204px; top: 76px; text-align: center; font-size: 26px; }
</style>
</head>
<body>

<!-- Side 1: residential / strata -->
<section class="page page--residential">
  <div class="title-block">Residential/<br>Strata<br>Building<br>Services</div>

  <div class="service-tile" style="left:240px;top:19px;">
    <svg width="42" height="42" viewBox="0 0 41 41"><path d="M8 33h25l-3-9H11z M18 24l3-15 3 1-3 14z" fill="#fff"/></svg>
  </div>
  <div class="line" style="left:300px;top:28px;">Cleaning</div>
  <div class="service-tile" style="left:240px;top:67px;">
    <svg width="42" height="42" viewBox="0 0 41 41"><path d="M16 8h9v8h8v9h-8v8h-9v-8H8v-9h8z" fill="#fff"/></svg>
  </div>
  <div class="line" style="left:300px;top:75px;">Caretaking</div>
  <div class="service-tile" style="left:240px;top:115px;">
    <svg width="42" height="42" viewBox="0 0 41 41"><circle cx="20.5" cy="13" r="6" fill="#fff"/><path d="M17 18h7l3 16H14z" fill="#fff"/></svg>
  </div>
  <div class="line" style="left:300px;top:123px;">Concierge</div>

  <svg class="icon" style="left:35px;top:164px;" width="125" height="110" viewBox="0 0 125 110" aria-hidden="true">
    <circle cx="48" cy="48" r="36" fill="none" stroke="var(--sky)" stroke-width="14" stroke-dasharray="11 8"/>
    <circle cx="48" cy="48" r="30" fill="none" stroke="var(--sky)" stroke-width="12"/>
    <circle cx="92" cy="75" r="23" fill="none" stroke="var(--sky)" stroke-width="10" stroke-dasharray="7 6"/>
    <circle cx="92" cy="75" r="19" fill="#fff" stroke="var(--sky)" stroke-width="9"/>
  </svg>
  <div class="line" style="left:207px;top:190px;">#1 Priority - Customer Service</div>
  <div class="line line--plain" style="left:210px;top:215px;">And communication</div>

  <svg class="icon" style="left:33px;top:284px;" width="102" height="75" viewBox="0 0 102 75" aria-hidden="true">
    <g fill="var(--sky)">
      <rect x="0" y="0" width="17" height="15" rx="2"/><rect x="21" y="0" width="17" height="15" rx="2"/><rect x="42" y="0" width="17" height="15" rx="2"/><rect x="63" y="0" width="17" height="15" rx="2"/><rect x="84" y="0" width="17" height="15" rx="2"/>
      <rect x="0" y="20" width="17" height="15" rx="2"/><rect x="21" y="20" width="17" height="15" rx="2"/><rect x="42" y="20" width="17" height="15" rx="2"/><rect x="63" y="20" width="17" height="15" rx="2"/><rect x="84" y="20" width="17" height="15" rx="2"/>
      <rect x="0" y="40" width="17" height="15" rx="2"/><rect x="21" y="40" width="17" height="15" rx="2"/><rect x="42" y="40" width="17" height="15" rx="2"/><rect x="63" y="40" width="17" height="15" rx="2"/><rect x="84" y="40" width="17" height="15" rx="2"/>
      <rect x="0" y="60" width="17" height="15" rx="2"/><rect x="21" y="60" width="17" height="15" rx="2"/><rect x="42" y="60" width="17" height="15" rx="2"/><rect x="63" y="60" width="17" height="15" rx="2"/><rect x="84" y="60" width="17" height="15" rx="2"/>
    </g>
  </svg>
  <div class="line" style="left:207px;top:296px;">Over 20 years industry experience</div>
  <div class="line" style="left:207px;top:321px;">Trained, couteous staff</div>

  <svg class="icon" style="left:54px;top:374px;" width="84" height="78" viewBox="0 0 84 78" aria-hidden="true">
    <path d="M10 2 C60 0 82 30 82 76 C70 52 50 48 26 46 C8 42 0 20 10 2z" fill="var(--sky)"/>
    <text x="30" y="34" fill="#fff" font-family="Roboto Condensed, sans-serif" font-size="15" font-weight="700" text-anchor="middle">100%</text>
  </svg>
  <div class="line" style="left:207px;top:387px;">100% Green Chemicals</div>
  <div class="line line--plain" style="left:207px;top:412px;">Servicing greater vancouver</div>

  <svg class="icon" style="left:58px;top:459px;" width="84" height="100" viewBox="0 0 84 100" aria-hidden="true">
    <path d="M30 50 L12 92 L24 86 L30 98 L44 56z" fill="var(--sky)"/>
    <path d="M46 56 L60 98 L66 86 L80 92 L58 50z" fill="var(--sky)"/>
    <circle cx="40" cy="34" r="28" fill="var(--sky-pale)"/>
    <circle cx="40" cy="34" r="21" fill="var(--sky)"/>
  </svg>
  <div class="line" style="left:207px;top:493px;">Affordable, quality service</div>

  <div class="contact-block">
    <div class="phone-small">CALL 604-555-0148</div>
    <div class="email">hello@harbortidyworks.com</div>
  </div>
  <div class="headline" style="top:605px;">New Construction?</div>
  <div class="headline" style="top:641px;">We do move-ins/outs</div>
</section>

<!-- Side 2: commercial -->
<section class="page page--commercial">
  <div class="title-block" style="padding-top:36px;">Commercial<br>Building<br>Services</div>

  <div class="line" style="left:232px;top:40px;">Daily or weekly service</div>
  <div class="line" style="left:232px;top:65px;">500 – 200,00 square feet</div>
  <div class="line" style="left:232px;top:90px;">100% Green Cleaning</div>

  <svg class="icon" style="left:44px;top:164px;" width="125" height="110" viewBox="0 0 125 110" aria-hidden="true">
    <circle cx="48" cy="48" r="36" fill="none" stroke="var(--sky)" stroke-width="14" stroke-dasharray="11 8"/>
    <circle cx="48" cy="48" r="30" fill="none" stroke="var(--sky)" stroke-width="12"/>
    <circle cx="92" cy="75" r="23" fill="none" stroke="var(--sky)" stroke-width="10" stroke-dasharray="7 6"/>
    <circle cx="92" cy="75" r="19" fill="#fff" stroke="var(--sky)" stroke-width="9"/>
  </svg>
  <div class="line" style="left:207px;top:190px;">Customized specifications</div>
  <div class="line" style="left:207px;top:215px;">Structured supervision</div>

  <svg class="icon" style="left:59px;top:283px;" width="76" height="76" viewBox="0 0 78 78" aria-hidden="true">
    <circle cx="39" cy="39" r="36" fill="var(--sky)"/>
    <circle cx="39" cy="39" r="28" fill="#fff"/>
    <circle cx="39" cy="39" r="25" fill="none" stroke="var(--sky)" stroke-width="2"/>
    <path d="M39 22 V40 H52" fill="none" stroke="var(--sky)" stroke-width="3"/>
  </svg>
  <div class="line" style="left:207px;top:297px;">24/7 Service</div>
  <div class="line" style="left:207px;top:321px;">365 days a week</div>

  <svg class="icon" style="left:59px;top:366px;" width="84" height="100" viewBox="0 0 84 100" aria-hidden="true">
    <path d="M30 50 L12 92 L24 86 L30 98 L44 56z" fill="var(--sky)"/>
    <path d="M46 56 L60 98 L66 86 L80 92 L58 50z" fill="var(--sky)"/>
    <circle cx="40" cy="34" r="28" fill="var(--sky-pale)"/>
    <circle cx="40" cy="34" r="21" fill="var(--sky)"/>
  </svg>
  <div class="line" style="left:207px;top:389px;">Systematic quality</div>
  <div class="line" style="left:207px;top:414px;">Assurance (QA)</div>

  <div class="icon" role="img" aria-label="Icon of an auditor at a desk" style="left:61px;top:477px;width:84px;height:76px;background:var(--sky);border-radius:40px 40px 0 0;"></div>
  <div class="line" style="left:207px;top:504px;">Audits</div>

  <div class="contact-block">
    <div class="call-label">CALL</div>
    <div class="call-number">604-555-0148</div>
  </div>
  <div class="line" style="left:232px;top:579px;">No more cleaning headaches!</div>
  <div class="line" style="left:232px;top:604px;">KLENA cleaning production rates</div>
  <div class="line" style="left:232px;top:628px;">20 years experience</div>
  <div class="line" style="left:232px;top:653px;">Affordable, quality service</div>
  <div class="line" style="left:232px;top:678px;">Trained,courteous staff</div>
</section>

</body>
</html>
```